Info flyer to showcase security camera install and remote video monitoring.

I am looking for an attractive looking flyer that is simple and has some text content and some photos to show prospective clients what services I can provide them.

The two main services that I want to showcase are:
1. Security Camera & NVR Installations and maintenance
2. Remote Video Monitoring for business. This can be a temporary service or ongoing/long term.

Target Market(s)

Construction, Retail, Industrial, Commercial

Industry/Entity Type

Security

Font styles to use
Serif

Colors

Designer to choose colors to be used in the design.

```html
<!DOCTYPE html>
<html lang="en">
<head>
<meta charset="utf-8">
<title>Halden Security Group – Security Flyer</title>
<link href="https://fonts.googleapis.com/css2?family=Saira+Condensed:wght@500;600&family=Quicksand:wght@600&family=Lato:wght@400&display=swap" rel="stylesheet">
<style>
  :root{
    --gold:#d4a21f;
    --charcoal:#3b3b3d;
    --band:#444446;
    --ink:#2f2f31;
    --body:#3a3a3a;
    --paper:#f1f1f1;
    --stage:#e6e6e6;
    --white:#ffffff;
  }
  *{margin:0;padding:0;box-sizing:border-box}
  html,body{width:1200px;height:1200px;overflow:hidden;background:var(--stage)}
  .canvas{position:relative;width:1200px;height:1200px}
  .flyer{
    position:absolute;left:215px;top:40px;width:685px;height:998px;
    transform:scale(1.1222);transform-origin:0 0;
    background:linear-gradient(160deg,#fafafa 0%,var(--paper) 55%,#e9e9e9 100%);
    overflow:hidden;box-shadow:0 6px 24px rgba(0,0,0,.18);
  }
  .flyer-shapes{position:absolute;inset:0;width:685px;height:998px}
  .brand{position:absolute;left:42px;top:92px;font-family:"Saira Condensed",sans-serif;font-weight:600;color:var(--charcoal);font-size:34px;line-height:1;letter-spacing:1px;text-transform:uppercase}
  .headline{position:absolute;left:40px;top:288px}
  .headline .accent{display:block;font-family:"Saira Condensed",sans-serif;font-weight:600;color:var(--gold);font-size:46px;line-height:46px;letter-spacing:.5px}
  .headline .soft{display:block;font-family:"Quicksand",sans-serif;font-weight:600;color:var(--charcoal);font-size:31px;line-height:42px;margin:0 0 4px}
  .services-tab{position:absolute;left:522px;top:442px;width:163px;height:30px;background:var(--gold);clip-path:polygon(10px 0,100% 0,100% 100%,0 100%);font-family:"Saira Condensed",sans-serif;font-weight:500;font-size:19px;color:var(--ink);line-height:30px;padding-left:14px}
  .service{position:absolute;right:40px;text-align:right}
  .service-head{display:flex;justify-content:flex-end;align-items:center;gap:10px}
  .service-title{font-family:"Saira Condensed",sans-serif;font-weight:500;font-size:19px;line-height:22px;color:var(--ink)}
  .service-icon{width:42px;height:34px}
  .service-body{font-family:"Lato",sans-serif;font-size:9.6px;line-height:13.6px;color:var(--body);margin-top:14px}
  .service--install{top:503px;width:450px}
  .service--monitoring{top:684px;width:410px}
  .contact{position:absolute;right:40px;text-align:right;font-family:"Lato",sans-serif;color:var(--white)}
  .contact-phone{top:910px;font-family:"Saira Condensed",sans-serif;font-weight:500;font-size:21px;display:flex;align-items:center;gap:6px}
  .contact-web{top:942px;font-size:10.5px;display:flex;align-items:center;gap:14px}
  .contact-web .site{letter-spacing:2px}
  .contact-web span{display:flex;align-items:center;gap:5px}
</style>
</head>
<body>
<main class="canvas">
  <article class="flyer">
    <svg class="flyer-shapes" viewBox="0 0 685 998">
      <defs>
        <linearGradient id="hero-fade" x1="0" y1="0" x2="1" y2="0">
          <stop offset="0" stop-color="#f4f4f4" stop-opacity="0"/>
          <stop offset=".35" stop-color="#d9dde2"/>
          <stop offset=".75" stop-color="#8f98a6"/>
          <stop offset="1" stop-color="#6b7484"/>
        </linearGradient>
        <linearGradient id="pole-fade" x1="0" y1="0" x2="0" y2="1">
          <stop offset="0" stop-color="#dfe1e4" stop-opacity="0"/>
          <stop offset=".3" stop-color="#cfd3d8"/>
          <stop offset="1" stop-color="#b9bec6"/>
        </linearGradient>
      </defs>
      <polygon role="img" aria-label="Photo of a dome security camera mounted in a busy shopping centre"
               points="0,0 685,0 685,360 570,390 155,190 0,250" fill="url(#hero-fade)"/>
      <polygon points="0,248 155,185 155,202 0,272" fill="var(--gold)"/>
      <polygon points="155,185 575,385 575,398 150,200" fill="var(--charcoal)"/>
      <polygon points="570,385 685,355 685,372 575,400" fill="var(--gold)"/>
      <polygon points="0,878 130,942 685,858 685,998 0,998" fill="var(--band)"/>
      <polygon points="0,870 130,936 685,852 685,862 130,946 0,884" fill="var(--gold)"/>
      <rect role="img" aria-label="Photo of a pole carrying a dome camera and a cluster of bullet security cameras"
            x="40" y="460" width="285" height="538" rx="6" fill="url(#pole-fade)"/>
    </svg>

    <header class="brand">Halden Security Group</header>

    <h1 class="headline">
      <span class="accent">SECURITY IS</span>
      <span class="soft">everyone’s concern...</span>
      <span class="accent">BUT IT’S OUR BUSINESS</span>
    </h1>

    <div class="services-tab">OUR SERVICES</div>

    <section class="service service--install">
      <div class="service-head">
        <h2 class="service-title">Security Camera &amp;<br>NVR Installations and maintenance</h2>
        <svg class="service-icon" viewBox="0 0 42 34"><g fill="var(--gold)"><polygon points="4,12 30,2 34,12 8,22"/><rect x="30" y="18" width="4" height="14"/><polygon points="20,17 32,23 31,26 18,20"/><circle cx="12" cy="25" r="4"/></g></svg>
      </div>
      <p class="service-body">Lorem Ipsum is simply dummy text of the printing and typesetting industry. Lorem Ipsum has been the industry’s standard dummy text ever since the 1500s, when an unknown printer took a galley of type and scrambled it to make a type specimen book. It has survived not only five centuries, but also the leap into electronic typesetting, remaining essentially unchanged. It was popularised in the 1960s with the release of Letraset sheets containing Lorem Ipsum passages, and more recently with desktop publishing software like Aldus PageMaker including versions of Lorem Ipsum.</p>
    </section>

    <section class="service service--monitoring">
      <div class="service-head">
        <h2 class="service-title">Remote Video Monitoring for business</h2>
        <svg class="service-icon" viewBox="0 0 42 34"><g fill="var(--gold)"><polygon points="4,12 30,2 34,12 8,22"/><rect x="30" y="18" width="4" height="14"/><polygon points="20,17 32,23 31,26 18,20"/><circle cx="12" cy="25" r="4"/></g></svg>
      </div>
      <p class="service-body">Lorem Ipsum is simply dummy text of the printing and typesetting industry. Lorem Ipsum has been the industry’s standard dummy text ever since the 1500s, when an unknown printer took a galley of type and scrambled it to make a type specimen book. It has survived not only five centuries, but also the leap into electronic typesetting, remaining essentially unchanged. It was popularised in the 1960s with the release of Letraset sheets containing Lorem Ipsum passages, and more recently with desktop publishing software like Aldus PageMaker including versions of Lorem Ipsum.</p>
    </section>

    <div class="contact contact-phone">0198 765 432
      <svg width="18" height="18" viewBox="0 0 18 18"><circle cx="9" cy="9" r="8" fill="none" stroke="var(--gold)" stroke-width="1.6"/><path d="M6 4.5c-1 1-1 3 .8 5.6 1.8 2.4 3.8 3.6 5 3l.8-1.4-2-1.4-1 .8c-.8-.4-1.8-1.6-2.2-2.4l.8-1-1.2-2.2z" fill="var(--gold)"/></svg>
    </div>
    <div class="contact contact-web">
      <span>hello@haldensecure.com
        <svg width="16" height="12" viewBox="0 0 16 12"><rect x="1" y="1" width="14" height="10" fill="none" stroke="var(--gold)" stroke-width="1.2"/><path d="M1 1l7 6 7-6" fill="none" stroke="var(--gold)" stroke-width="1.2"/></svg>
      </span>
      <span class="site">www.haldensecure.com
        <svg width="18" height="18" viewBox="0 0 18 18"><g fill="none" stroke="var(--gold)" stroke-width="1.4"><circle cx="9" cy="9" r="7.5"/><ellipse cx="9" cy="9" rx="3.2" ry="7.5"/><path d="M1.5 9h15M3 5h12M3 13h12"/></g></svg>
      </span>
    </div>
  </article>
</main>
</body>
</html>
```